Visitenkarten für eine Hypnose-Praxis
Ich bin sehr zufrieden mit der professionellen Arbeitsweise von KOR2874. Es war immer ein netter Kontakt und meine Wünsche wurden schnell umgesetzt. Alle Vorschläge waren sehr kreativ und und so viel es mir leicht, eine schnelle Entscheidung zu treffen.
Zielgruppe
Wir sind eine Hypnose-Praxis und richten unser Angebot an Privatpersonen unterschiedlichen Alters, die therapeutische Unterstützung suchen.
Aufgabenstellung
Eher schlichtes und modernes Design

```html
<!DOCTYPE html>
<html lang="de">
<head>
<meta charset="utf-8">
<title>Visitenkarten Hypnose-Praxis</title>
<link href="https://fonts.googleapis.com/css2?family=Figtree:wght@400;500;700&display=swap" rel="stylesheet">
<style>
  :root {
    --backdrop: #3a8bb2;
    --card: #ffffff;
    --ink: #2a2a2a;
    --teal: #1aa6a0;
    --brand-square: #45abc9;
  }
  html, body {
    margin: 0;
    padding: 0;
    width: 1200px;
    height: 877px;
    overflow: hidden;
    background: var(--backdrop);
    font-family: "Figtree", sans-serif;
  }
  .stage {
    position: relative;
    width: 1200px;
    height: 877px;
  }
  .card {
    position: absolute;
    top: 324px;
    width: 468px;
    height: 303px;
    background: var(--card);
    color: var(--ink);
  }
  .card--front { left: 114px; }
  .card--back { left: 649px; width: 470px; }

  .holder {
    position: absolute;
    left: 27px;
    top: 26px;
  }
  .holder__name {
    margin: 0;
    font-size: 20px;
    font-weight: 700;
    line-height: 24px;
  }
  .holder__titles {
    margin: 1px 0 0;
    padding: 0;
    list-style: none;
    color: var(--teal);
    font-size: 14.5px;
    font-weight: 400;
    line-height: 19px;
  }

  .contact {
    position: absolute;
    left: 247px;
    top: 138px;
    font-size: 14.5px;
    line-height: 17.5px;
  }
  .contact p { margin: 0 0 17px; }
  .contact p:last-child { margin: 0; }

  .brand {
    display: flex;
    align-items: center;
    gap: 10px;
  }
  .brand__square {
    background: var(--brand-square);
    border-radius: 3px;
  }
  .brand__name {
    font-weight: 500;
    color: var(--ink);
    letter-spacing: -0.5px;
  }
  .brand--small {
    position: absolute;
    left: 27px;
    top: 208px;
  }
  .brand--small .brand__square { width: 22px; height: 22px; }
  .brand--small .brand__name { font-size: 34px; line-height: 40px; }

  .brand--large {
    position: absolute;
    left: 0;
    right: 0;
    top: 118px;
    justify-content: center;
    gap: 16px;
  }
  .brand--large .brand__square { width: 34px; height: 34px; border-radius: 4px; }
  .brand--large .brand__name { font-size: 56px; line-height: 64px; }
</style>
</head>
<body>
<main class="stage">
  <section class="card card--front">
    <header class="holder">
      <h1 class="holder__name">Lukas Brenner</h1>
      <ul class="holder__titles">
        <li>Diplom-Psychologe</li>
        <li>Heilpraktiker für Psychotherapie</li>
        <li>Spezialisierung Hypnose-Therapie</li>
      </ul>
    </header>
    <div class="brand brand--small">
      <span class="brand__square"></span>
      <span class="brand__name">tiefenruh</span>
    </div>
    <address class="contact" style="font-style:normal">
      <p>Gartenweg 14,<br>10115 Berlin</p>
      <p>Tel: 030 55120487<br>24-Std-AB: 030 55120499</p>
      <p>info@tiefenruh-praxis.de<br>www.tiefenruh-praxis.de</p>
    </address>
  </section>

  <section class="card card--back">
    <div class="brand brand--large">
      <span class="brand__square"></span>
      <span class="brand__name">tiefenruh</span>
    </div>
  </section>
</main>
</body>
</html>
```